Web Design Pell Marrow

• An Overview of Pell Marrow for reference: We use to be a component manufacturing company. We sold to customers in USA and manage the builds in China using many manufacturing partners. We had a web site that served this market but we have transitioned over the last several years into “A unique design, development and program management company” It is this message we want to put up on the web now. We provide the design support, we help develop and test a new product for our customers and we provide the manufactured produce once we have transitioned it into production.
• The Target Market: Our customers are all high tech. Each product we produce is custom designed and sold only to one a specific customer. We work with a limited number of customer and sell to new customers by word of mouth and referrals. The web site is to provide a back ground check of any new referral so they can see who we are and our basic capabilities. It is not designed to sell customers or to find new customers but provide a background check to new potential customers.
• Pages Required: We estimate 12:
o Home/Title page is page 1 of PDF. It would have buttons to select other pages
o Names of other pages would be (short titles below if on button, if pull down menu the full title of slide)
 USA Facilities
 China Facilities
 Enclosures
 Antennas
 Connectors
 Cables
 EMI Shields
 Overlays
 Process Development
 Voxtrel
 Contact Us (???) >> new page which we are not sure if we should or should not add.
• Design Specifics; attached is our logo, a PDF and PowerPoint slides showing the views we desire. We like these layouts, but perhaps a better one may be suggested for some artistic reason or layout. It should be clean, simple and user intuitive. We like the off white background and use for most of our presentations. One should be able to go from any screen to any other screen. The quote must include both design and implementation onto our web site which is http://pellmarrowsystems.com/
• Design Process:
We would like to see concepts of the Landing/Homepage, and an internal page initially. Feedback will be provided and you will be asked to continue if your layout is on the correct track.

• Implementation: Desire designer/implimentor to set up on their server. Allow us to test and edit on their site. We will provide password for implementation on our site after final approval.

Target Market(s)

• The Target Market: see above task descripiton

Industry/Entity Type

It Company

Requirements
Must have
• • Pages Required: We estimate 12:
 USA Facilities
 China Facilities
 Enclosures
 Antennas
 Connectors
 Cables
 EMI Shields
 Overlays
 Process Development
 Voxtrel

Must have the implementation phase include in quote. see task description above
Should not have
• Should not be complex or long time loading.
Do not want any twitter or promotional add on functions.

```html
<!DOCTYPE html>
<html lang="en">
<head>
<meta charset="utf-8">
<title>Pell Marrow — Design, Development and Program Management</title>
<link rel="stylesheet" href="https://fonts.googleapis.com/css2?family=Ubuntu:wght@400;500;700&display=swap">
<style>
  :root {
    --page-top: #000000;
    --page-mid: #9a9a9a;
    --page-bottom: #e8e8e8;
    --panel-top: #0a56a6;
    --panel-bottom: #2fa2ee;
    --white: #ffffff;
    --button-top: #dcdcdc;
    --button-bottom: #fbfbfb;
    --button-active-top: #8fd8fb;
    --button-active-bottom: #fdfeff;
    --button-text: #666a70;
    --map-tone: #eef3f9;
    --photo-tone: #8a8680;
  }
  * { box-sizing: border-box; margin: 0; padding: 0; }
  html, body { width: 1200px; height: 998px; overflow: hidden; }
  body {
    font-family: "Ubuntu", sans-serif;
    background: linear-gradient(to bottom, var(--page-top) 0, #2a2a2a 60px, var(--page-mid) 380px, var(--page-bottom) 620px, var(--page-bottom) 100%);
    position: relative;
  }
  .site-panel {
    position: absolute;
    left: 125px; top: 0;
    width: 943px; height: 998px;
    background: linear-gradient(to bottom, var(--panel-top) 0, #1679cf 450px, var(--panel-bottom) 100%);
  }
  .brand {
    position: absolute;
    left: 35px; top: 20px;
    width: 184px; height: 186px;
    background: var(--white);
    display: flex; align-items: center; justify-content: center; gap: 10px;
    border: 6px solid var(--white);
    outline: 3px solid var(--panel-top);
    outline-offset: -9px;
  }
  .brand-mark { width: 16px; height: 16px; background: var(--panel-top); }
  .brand-name {
    font-weight: 700; font-size: 27px; line-height: 1.05;
    color: var(--panel-top); text-align: left;
  }
  .contact-link {
    position: absolute; right: 33px; top: 15px;
    color: var(--white); font-size: 10px; text-decoration: none;
    display: flex; align-items: center; gap: 4px;
  }
  .tagline {
    position: absolute; left: 35px; top: 230px;
    color: var(--white); line-height: 1.2;
  }
  .tagline .lead { font-size: 29px; font-weight: 500; display: block; }
  .tagline .rest { font-size: 24px; display: block; }
  .world-map {
    position: absolute; left: 290px; top: 16px;
    width: 606px; height: 372px;
    background: radial-gradient(ellipse at 55% 50%, var(--map-tone) 0, rgba(238,243,249,0.55) 55%, rgba(238,243,249,0) 75%);
    border-radius: 40px;
  }
  .photo-strip {
    position: absolute; left: 33px; top: 421px;
    display: flex; gap: 14px;
  }
  .photo-frame {
    width: 210px; height: 135px;
    background: var(--white);
    padding: 7px 8px;
    box-shadow: 0 1px 3px rgba(0,0,0,0.3);
  }
  .photo-fill { width: 100%; height: 100%; background: linear-gradient(135deg, #b9b4a8, var(--photo-tone)); }
  .photo-fill.warehouse { background: linear-gradient(135deg, #c8a98a, #7a6a5c); }
  .photo-fill.lab { background: linear-gradient(135deg, #d7dde2, #5d6166); }
  .photo-fill.office { background: linear-gradient(135deg, #cfd4d6, #6f7a74); }
  .section-nav {
    position: absolute; left: 35px; top: 579px;
    display: grid;
    grid-template-columns: 431px 431px;
    column-gap: 16px; row-gap: 17px;
  }
  .nav-button {
    height: 63px;
    display: flex; align-items: center; justify-content: center;
    background: linear-gradient(to bottom, var(--button-top), var(--button-bottom));
    border-radius: 3px;
    box-shadow: 0 1px 2px rgba(0,0,0,0.35);
    color: var(--button-text);
    font-size: 26px; text-decoration: none;
  }
  .nav-button.is-active {
    background: linear-gradient(to bottom, var(--button-active-top), var(--button-active-bottom));
  }
</style>
</head>
<body>
  <main class="site-panel">
    <div class="brand">
      <span class="brand-mark"></span>
      <span class="brand-name">Pell<br>Marrow</span>
    </div>

    <a class="contact-link" href="http://pellmarrowsystems.com/">
      <svg width="12" height="9" viewBox="0 0 12 9" aria-hidden="true">
        <rect x="0.5" y="0.5" width="11" height="8" fill="none" stroke="#fff"/>
        <polyline points="0.5,0.5 6,5 11.5,0.5" fill="none" stroke="#fff"/>
      </svg>
      Contact
    </a>

    <p class="tagline">
      <span class="lead">A unique design,</span>
      <span class="rest">\development and program</span>
      <span class="rest">management company</span>
    </p>

    <div class="world-map" role="img" aria-label="World map with location pins highlighting the USA, Brazil, Europe, Russia and Australia"></div>

    <div class="photo-strip">
      <div class="photo-frame"><div class="photo-fill" role="img" aria-label="Aerial view of the industrial facility"></div></div>
      <div class="photo-frame"><div class="photo-fill warehouse" role="img" aria-label="Warehouse shelves stocked with boxes"></div></div>
      <div class="photo-frame"><div class="photo-fill lab" role="img" aria-label="Technician testing a part at a lab bench"></div></div>
      <div class="photo-frame"><div class="photo-fill office" role="img" aria-label="Engineer presenting stacked component trays"></div></div>
    </div>

    <nav class="section-nav">
      <a class="nav-button is-active" href="#">USA Facilities</a>
      <a class="nav-button" href="#">China Facilities</a>
      <a class="nav-button" href="#">Enclosures</a>
      <a class="nav-button" href="#">Antennas</a>
      <a class="nav-button" href="#">Connectors</a>
      <a class="nav-button" href="#">Cables</a>
      <a class="nav-button" href="#">EMI Shields</a>
      <a class="nav-button" href="#">Overlays</a>
      <a class="nav-button" href="#">Process Development</a>
      <a class="nav-button" href="#">Voxtrel</a>
    </nav>
  </main>
</body>
</html>
```